Moravel IT Customer Focused Solutions 1 Page Overview

We are looking to create a 1-page overview of our customer's IT challenges, how we assist them in resolving them, and allow their business to grow. Moravel IT, helps our customers secure their systems, minimize downtime, and allow them to focus on engaging their customer base instead of focusing on IT issues. The final design should communicate that we are safe pair of hands to manage their IT which allows them to focus on their business.

Target Market(s)

Small to Mid Size Business Owners

Industry/Entity Type

It Company

Font styles to use
Sans Serif

Requirements
Must have
• Company Logo, colour scheme that matches our logo colour, mixed with easy to read items

```html
<!DOCTYPE html>
<html lang="en">
<head>
<meta charset="utf-8">
<title>Moravel IT – Customer Focused Solutions</title>
<link href="https://fonts.googleapis.com/css2?family=Montserrat:wght@400;500;600;700;800&family=Open+Sans:wght@400;600;700&display=swap" rel="stylesheet">
<style>
:root{
  --orange:#e8761c;
  --orange-dark:#b95d14;
  --orange-deep:#8a4510;
  --ink:#2b2b2b;
  --muted:#6a6a6a;
  --line:#e6e6e6;
  --paper:#ffffff;
  --soft:#f6f6f6;
}
*{box-sizing:border-box;margin:0;padding:0}
html,body{width:1200px;height:3012px;overflow:hidden}
body{font-family:"Open Sans",Arial,sans-serif;color:var(--ink);background:var(--paper);position:relative}
h1,h2,h3,h4,.brand,.nav a,.btn{font-family:"Montserrat",Arial,sans-serif}

/* header */
.site-header{position:absolute;top:0;left:0;width:1200px;height:72px;background:var(--paper);display:flex;align-items:center;padding:0 120px;z-index:3;box-shadow:0 1px 4px rgba(0,0,0,.08)}
.brand{display:flex;align-items:center;gap:10px;font-weight:700;font-size:30px;color:var(--orange)}
.brand-dot{width:26px;height:26px;border-radius:50%;background:var(--orange)}
.nav{margin-left:auto;display:flex;gap:34px}
.nav a{font-size:13px;font-weight:700;color:var(--ink);text-decoration:none;letter-spacing:.3px}
.nav a.active{color:var(--orange);border-bottom:2px solid var(--orange);padding-bottom:4px}

/* hero */
.hero{position:absolute;top:0;left:0;width:1200px;height:592px;background:linear-gradient(120deg,#6b6157 0%,#c86a24 45%,#e8761c 70%,#a25a26 100%)}
.hero-content{position:absolute;top:340px;left:0;width:1200px;text-align:center;color:#fff}
.hero h1{font-size:50px;font-weight:700;letter-spacing:-.5px;text-shadow:0 2px 8px rgba(0,0,0,.3)}
.hero p{font-size:19px;margin-top:10px;font-weight:600}
.btn{display:inline-block;background:var(--orange);color:#fff;font-weight:700;font-size:14px;padding:14px 30px;border-radius:3px;text-decoration:none}
.hero .btn{margin-top:34px}

/* services */
.services{position:absolute;top:600px;left:0;width:1200px;height:440px;text-align:center}
.section-title{font-size:34px;font-weight:700;color:var(--ink);display:flex;justify-content:center;align-items:center;gap:12px}
.title-mark{width:26px;height:26px;border-radius:50%;background:var(--orange)}
.services .section-title{margin-top:56px}
.services .lead{font-size:21px;font-weight:700;margin-top:20px}
.service-cards{display:flex;justify-content:center;gap:16px;margin-top:40px}
.service-card{width:230px;height:240px;background:var(--paper);border:1px solid var(--line);box-shadow:0 2px 8px rgba(0,0,0,.06);padding:28px 20px}
.service-card svg{width:52px;height:52px}
.service-card h3{font-size:14px;font-weight:700;margin-top:16px}
.service-card p{font-size:11px;color:var(--muted);margin-top:8px;line-height:1.5}
.service-card .more{display:block;font-family:"Montserrat",Arial,sans-serif;font-size:11px;font-weight:700;color:var(--orange);margin-top:14px}

/* excellence */
.excellence{position:absolute;top:1048px;left:0;width:1200px;height:440px;background:var(--soft)}
.excellence-photo{position:absolute;left:0;top:0;width:700px;height:440px;background:linear-gradient(135deg,#d9dcde 0%,#eef0f1 40%,#b7bcc0 70%,#e8761c 71%,#c85f14 100%)}
.excellence-panel{position:absolute;left:640px;top:40px;width:560px;height:360px;background:var(--paper);padding:36px 40px;box-shadow:0 4px 14px rgba(0,0,0,.08)}
.excellence-panel h2{font-size:32px;font-weight:700;line-height:1.2}
.excellence-panel p{font-size:11px;color:var(--muted);line-height:1.6;margin-top:14px}
.excellence-panel .btn{margin-top:22px;padding:10px 22px;font-size:12px}

/* mission */
.mission{position:absolute;top:1528px;left:0;width:1200px;height:190px;background:linear-gradient(90deg,#8a4510,#d06a1a 30%,#e8761c 55%,#b95d14 80%,#7a3d0e);text-align:center;color:#fff;padding-top:42px}
.mission h2{font-size:30px;font-weight:700}
.mission p{font-size:17px;max-width:800px;margin:16px auto 0;line-height:1.45}

/* turbocharge */
.turbo{position:absolute;top:1740px;left:0;width:1200px;height:1060px;text-align:center}
.turbo h2{font-size:32px;font-weight:700;display:inline-block;border-bottom:2px solid var(--ink);padding-bottom:6px}
.turbo h3{font-size:24px;font-weight:700;margin-top:30px}
.turbo p{font-size:13px;color:var(--muted);margin-top:12px}
.hex-grid{position:absolute;left:0;top:150px;width:1200px;height:700px}
.hex-label{font-family:"Montserrat",Arial,sans-serif;font-size:27px;font-weight:600;fill:#fff}
.turbo .btn{position:absolute;top:975px;left:530px;padding:12px 34px;font-size:13px}

/* footer */
.site-footer{position:absolute;top:2816px;left:0;width:1200px;height:196px;background:linear-gradient(90deg,#a4520f,#c46718 50%,#a4520f);color:#fff;padding:18px 120px 0}
.footer-cols{display:flex;gap:40px}
.footer-col{width:220px;font-size:11px;line-height:1.7}
.footer-col h4{font-size:11px;font-weight:700;letter-spacing:.5px;margin-bottom:6px}
.contact-row{display:flex;align-items:center;gap:8px}
.contact-row svg{width:14px;height:14px}
.social{display:flex;gap:8px;margin-top:6px}
.social span{width:20px;height:20px;border-radius:50%;border:1px solid #fff}
.footer-form{width:280px}
.footer-form .row{display:flex;gap:6px;margin-top:6px}
.field{flex:1;height:20px;background:#fff;border-radius:2px}
.field.area{height:30px}
.footer-form .send{margin-top:6px;height:22px;background:var(--orange-deep);color:#fff;font-size:10px;font-weight:700;text-align:center;line-height:22px;font-family:"Montserrat",Arial,sans-serif}
.copyright{position:absolute;bottom:8px;left:0;width:1200px;text-align:center;font-size:10px;opacity:.85}
</style>
</head>
<body>

<header class="site-header">
  <div class="brand"><span class="brand-dot"></span>Moravel</div>
  <nav class="nav">
    <a class="active">HOME</a><a>ABOUT US</a><a>SOLUTIONS &amp; SERVICES</a><a>TURBOCHARGE</a><a>OUR SERVICES</a><a>CONTACT US</a>
  </nav>
</header>

<section class="hero" role="img" aria-label="Team of IT staff working at computer screens, tinted orange">
  <div class="hero-content">
    <h1>Constant innovation around our IT services</h1>
    <p>We do what most IT companies only claim: simplify, save money and deliver value to your customers</p>
    <a class="btn">Find out more</a>
  </div>
</section>

<section class="services">
  <h2 class="section-title"><span class="title-mark"></span>Our Services</h2>
  <p class="lead">Your goals are too important to be weighed down by IT problems.</p>
  <div class="service-cards">
    <article class="service-card">
      <svg viewBox="0 0 52 52" fill="none" stroke="#e8761c" stroke-width="2.5"><circle cx="18" cy="16" r="7"/><path d="M6 40c0-8 5-13 12-13s12 5 12 13"/><rect x="30" y="24" width="16" height="12" rx="1"/><path d="M34 40h8"/></svg>
      <h3>Managed IT Services</h3>
      <p>IT support to keep your team working and systems running smoothly every single day.</p>
      <span class="more">READ MORE</span>
    </article>
    <article class="service-card">
      <svg viewBox="0 0 52 52" fill="none" stroke="#e8761c" stroke-width="2.5"><path d="M26 6l16 6v12c0 11-7 18-16 22-9-4-16-11-16-22V12z"/><rect x="19" y="24" width="14" height="11"/><path d="M22 24v-4a4 4 0 018 0v4"/></svg>
      <h3>Security</h3>
      <p>Protect your data from threats, attacks and unexpected downtime with layered defences.</p>
      <span class="more">READ MORE</span>
    </article>
    <article class="service-card">
      <svg viewBox="0 0 52 52" fill="none" stroke="#e8761c" stroke-width="2.5"><path d="M14 34a9 9 0 010-18 12 12 0 0123-2 9 9 0 011 20z"/><path d="M26 22v14M20 30l6 6 6-6"/></svg>
      <h3>Storage &amp; Management</h3>
      <p>Centralise your files, backups and cloud storage so nothing important gets lost.</p>
      <span class="more">READ MORE</span>
    </article>
    <article class="service-card">
      <svg viewBox="0 0 52 52" fill="none" stroke="#e8761c" stroke-width="2.5"><path d="M10 42l12-12M22 30l8 2 12-12-10-10-12 12z"/><circle cx="34" cy="18" r="3"/><path d="M14 28l-4 4M24 38l-4 4"/></svg>
      <h3>Technology Consulting Services</h3>
      <p>Planning and expert advice so every technology investment supports business growth.</p>
      <span class="more">READ MORE</span>
    </article>
  </div>
</section>

<section class="excellence">
  <div class="excellence-photo" role="img" aria-label="Close-up of a keyboard with an orange IT Service key"></div>
  <div class="excellence-panel">
    <h2>We deliver results and are obsessed with excellence.</h2>
    <p>Our IT services focus on a simple idea: your systems should work quietly in the background so you can focus on your customers. We plan, monitor and support your technology, resolving issues before they slow your team down.</p>
    <p>We measure success by your uptime, your security and your growth. Every client gets clear reporting, responsive support and a team that takes ownership of the outcome.</p>
    <p>We believe a reliable partner brings peace of mind, and excellence is the bar we set.</p>
    <a class="btn">Read more</a>
  </div>
</section>

<section class="mission" role="img" aria-label="Orange circuit board pattern background">
  <h2>Our Mission</h2>
  <p>To be the leading supplier of pathways, education, employment and learning for Indigenous people within the IT and Cyber Security sectors by 2025.</p>
</section>

<section class="turbo">
  <h2>Turbocharge your business</h2>
  <h3>Are you tired of the same old service?</h3>
  <p>The Moravel IT Team isn't just here to fix problems, we are here to help your business move faster and grow with confidence.</p>
  <p>Take an in-depth look at our TURBOCHARGE services if you need outstanding support today.</p>
  <svg class="hex-grid" viewBox="0 0 1200 700" role="img" aria-label="Honeycomb of orange-tinted photos showing each turbocharge service">
    <defs>
      <linearGradient id="hexFill" x1="0" y1="0" x2="1" y2="1">
        <stop offset="0" stop-color="#f0a25a"/><stop offset="1" stop-color="#c9671c"/>
      </linearGradient>
    </defs>
    <g fill="url(#hexFill)" stroke="#fff" stroke-width="6">
      <polygon points="444,35 604,127 604,313 444,405 284,313 284,127"/>
      <polygon points="756,35 916,127 916,313 756,405 596,313 596,127"/>
      <polygon points="288,325 448,417 448,603 288,695 128,603 128,417"/>
      <polygon points="600,325 760,417 760,603 600,695 440,603 440,417"/>
      <polygon points="912,325 1072,417 1072,603 912,695 752,603 752,417"/>
    </g>
    <g class="hex-label" text-anchor="middle">
      <text x="444" y="212">Support</text><text x="444" y="246">Desk</text>
      <text x="756" y="212">Advanced</text><text x="756" y="246">Security</text>
      <text x="288" y="502">Server</text><text x="288" y="536">Back ups</text>
      <text x="600" y="484">Dedicated</text><text x="600" y="518">Service Delivery</text><text x="600" y="552">Manager</text>
      <text x="912" y="502">Quarterly</text><text x="912" y="536">Reviews</text>
    </g>
  </svg>
  <a class="btn">Turbocharge</a>
</section>

<footer class="site-footer">
  <div class="footer-cols">
    <div class="footer-col">
      <h4>QUICK NAVIGATION</h4>
      Home<br>About Us<br>Solutions &amp; Services<br>Turbocharge<br>Our Services<br>Contact Us
    </div>
    <div class="footer-col">
      <h4>COMPANY INFORMATION</h4>
      Privacy Policy<br>Terms of Service<br>Careers<br>
      <h4 style="margin-top:6px">FOLLOW US</h4>
      <div class="social"><span></span><span></span><span></span><span></span></div>
    </div>
    <div class="footer-col">
      <h4>CONTACT US</h4>
      <div class="contact-row"><svg viewBox="0 0 14 14" fill="#fff"><path d="M3 1l2 3-1 2c1 2 2 3 4 4l2-1 3 2-1 2C6 13 1 8 1 3z"/></svg>(02) 5550 1842</div>
      <div class="contact-row"><svg viewBox="0 0 14 14" fill="#fff"><path d="M7 1a4 4 0 014 4c0 3-4 8-4 8S3 8 3 5a4 4 0 014-4zm0 2.5a1.5 1.5 0 100 3 1.5 1.5 0 000-3z"/></svg>14 Harbour Lane, Eastvale</div>
      <div class="contact-row"><svg viewBox="0 0 14 14" fill="none" stroke="#fff" stroke-width="1.4"><rect x="1" y="3" width="12" height="8"/><path d="M1 3l6 5 6-5"/></svg>hello@moravelit.example</div>
    </div>
    <div class="footer-form">
      <h4 style="font-size:11px;font-weight:700">KEEP IN TOUCH</h4>
      <div style="font-size:10px;line-height:1.4">Send us a message and our team will get back to you within one business day.</div>
      <div class="row"><div class="field"></div><div class="field"></div></div>
      <div class="row"><div class="field"></div><div class="field"></div></div>
      <div class="row"><div class="field area"></div></div>
      <div class="send">Send message</div>
    </div>
  </div>
  <div class="copyright">Copyright © Moravel IT</div>
</footer>

</body>
</html>
```